Land Buying Company Needs Letterhead for Direct Mail Marketing to Land Owners

We are looking for a professional letterhead that we will be including in our direct mail marketing. We will be sending this to land owners who may be interested in selling or purchasing land.

The letterhead needs to be editable. Headers and footers would look nice, but we are open. We would want it to include our address, website, phone, and email info. For right now the address to use for design purposes would the following:

Address: 415 Bramwell Avenue #600
Dallas, TX 75219
Website - www.quillridgeacres.example
Email - info@quillridgeacres.example
Phone - 866-402-ACRE

I have attached our logo zip file that we just had done on Pixel Guild. Let me know what questions you have, and thank you.

```html
<!DOCTYPE html>
<html lang="en">
<head>
<meta charset="utf-8">
<title>Quill Ridge Acres Letterhead</title>
<link href="https://fonts.googleapis.com/css2?family=Montserrat:wght@600&family=Roboto+Condensed:wght@400&display=swap" rel="stylesheet">
<style>
  :root {
    --forest: #3f6b1f;
    --leaf: #8dc63f;
    --backdrop: #e4e5e7;
    --paper: #ffffff;
    --ink: #3a3a3a;
    --mark-faint: #e8e8e8;
  }
  html, body {
    margin: 0;
    width: 1200px;
    height: 1200px;
    overflow: hidden;
    background: var(--backdrop);
  }
  .letterhead {
    position: absolute;
    left: 204px;
    top: 40px;
    width: 792px;
    height: 1120px;
    background: var(--paper);
    overflow: hidden;
  }
  .rule { position: absolute; }
  .rule--header { left: 313px; top: 24px; width: 479px; height: 7px; background: var(--forest); }
  .rule--side { left: 781px; top: 177px; width: 2px; height: 920px; background: var(--leaf); }
  .rule--footer-dark { left: 80px; top: 1097px; width: 460px; height: 5px; background: var(--forest); }
  .rule--footer-light { left: 317px; top: 1105px; width: 475px; height: 5px; background: var(--leaf); }

  .brand {
    position: absolute;
    left: 240px;
    top: 31px;
    display: flex;
    align-items: center;
    gap: 14px;
  }
  .brand__dot {
    width: 60px;
    height: 60px;
    border-radius: 50%;
    background: var(--forest);
  }
  .brand__name {
    font-family: "Montserrat", sans-serif;
    font-weight: 600;
    font-size: 30px;
    letter-spacing: 1px;
    color: var(--leaf);
    text-transform: uppercase;
  }

  .backdrop-mark {
    position: absolute;
    left: 265px;
    top: 409px;
    width: 300px;
    height: 300px;
    border-radius: 50%;
    background: var(--mark-faint);
  }

  .contact {
    position: absolute;
    right: 14px;
    top: 1012px;
    margin: 0;
    padding: 0;
    list-style: none;
    font-family: "Roboto Condensed", sans-serif;
    font-weight: 400;
    font-size: 11px;
    line-height: 1;
    color: var(--ink);
  }
  .contact__item {
    display: flex;
    justify-content: flex-end;
    align-items: center;
    gap: 8px;
    height: 20px;
  }
  .contact__icon { width: 13px; height: 13px; flex: none; }
  .contact__icon * { fill: none; stroke: var(--leaf); stroke-width: 2; }
  .contact__icon .solid { fill: var(--leaf); stroke: none; }
</style>
</head>
<body>
  <main class="letterhead">
    <div class="rule rule--header"></div>

    <header class="brand">
      <div class="brand__dot"></div>
      <span class="brand__name">Quill Ridge Acres</span>
    </header>

    <div class="rule rule--side"></div>
    <div class="backdrop-mark"></div>

    <ul class="contact">
      <li class="contact__item">866-402-ACRE
        <svg class="contact__icon" viewBox="0 0 24 24"><path class="solid" d="M6.6 10.8a15 15 0 0 0 6.6 6.6l2.2-2.2a1 1 0 0 1 1-.25 11.4 11.4 0 0 0 3.6.57 1 1 0 0 1 1 1V20a1 1 0 0 1-1 1A17 17 0 0 1 3 4a1 1 0 0 1 1-1h3.5a1 1 0 0 1 1 1c0 1.250.2 2.45.57 3.57a1 1 0 0 1-.25 1z"/></svg>
      </li>
      <li class="contact__item">info@quillridgeacres.example
        <svg class="contact__icon" viewBox="0 0 24 24"><rect x="2" y="5" width="20" height="14"/><path d="M2 5l10 8 10-8"/></svg>
      </li>
      <li class="contact__item">www.quillridgeacres.example
        <svg class="contact__icon" viewBox="0 0 24 24"><circle cx="12" cy="12" r="10"/><path d="M2 12h20M12 2c3 3 3 17 0 20M12 2c-3 3-3 17 0 20"/></svg>
      </li>
      <li class="contact__item">415 Bramwell Avenue #600, Dallas, TX 75219
        <svg class="contact__icon" viewBox="0 0 24 24"><path class="solid" d="M12 1a8 8 0 0 0-8 8c0 6 8 14 8 14s8-8 8-14a8 8 0 0 0-8-8zm0 11a3 3 0 1 1 0-6 3 3 0 0 1 0 6z"/></svg>
      </li>
    </ul>

    <div class="rule rule--footer-dark"></div>
    <div class="rule rule--footer-light"></div>
  </main>
</body>
</html>
```